Barrister Letterhead incorporating existing logo/design

Require new letterhead template to incorporate logo and information on 'Letter 2015' word document. Currently the information on the letterhead is very busy and would like a cleaner look.
Must look good in black and white, and colour when printed.

Target Market(s)

Professional

Industry/Entity Type

Legal

Requirements
Must have
• Clean professional look.

```html
<!DOCTYPE html>
<html lang="en">
<head>
<meta charset="utf-8">
<title>Harlow Chambers Letterhead</title>
<link rel="stylesheet" href="https://fonts.googleapis.com/css2?family=Cormorant+Garamond:wght@500&family=Open+Sans:wght@500&display=swap">
<style>
  :root {
    --navy: #1c2a4a;
    --grey: #8a8a8a;
    --ink: #2b2b2b;
    --green-deep: #0a3a08;
    --green-bright: #3fbf1a;
    --black: #020802;
    --paper: #ffffff;
  }
  * { margin: 0; padding: 0; box-sizing: border-box; }
  html, body { width: 960px; height: 1200px; overflow: hidden; background: var(--paper); }
  .letterhead { position: relative; width: 960px; height: 1200px; background: var(--black); overflow: hidden; }
  .top-band {
    position: absolute; left: 0; top: 0; width: 960px; height: 34px;
    background: linear-gradient(180deg, #0e6a0a 0%, var(--green-deep) 45%, var(--black) 100%);
  }
  .side-band {
    position: absolute; left: 0; top: 0; width: 108px; height: 1200px;
    background: linear-gradient(90deg, #1f8f0f 0%, var(--green-bright) 6%, #167a0b 14%, var(--black) 30%, var(--black) 55%, #0d5a08 78%, #1e8e10 100%);
  }
  .page {
    position: absolute; left: 108px; top: 34px; width: 852px; height: 1166px;
    background: var(--paper);
  }
  .brand { position: absolute; left: 61px; top: 20px; display: flex; align-items: flex-start; }
  .brand-square { width: 98px; height: 65px; background: var(--navy); margin-right: 20px; }
  .brand-name {
    font-family: "Cormorant Garamond", serif; font-weight: 500; color: var(--navy);
    font-size: 47px; line-height: 1; letter-spacing: 1.5px; margin-top: -4px;
    padding-bottom: 4px; border-bottom: 1px solid var(--grey); width: 538px;
  }
  .brand-tagline {
    font-family: "Cormorant Garamond", serif; font-weight: 500; color: var(--grey);
    font-size: 33px; line-height: 1; letter-spacing: 7.6px; margin-top: 2px;
  }
  .contact {
    position: absolute; top: 108px;
    font-family: "Open Sans", sans-serif; font-weight: 500; color: var(--ink);
    font-size: 14px; line-height: 21px; list-style: none;
  }
  .contact-left { left: 61px; top: 110px; }
  .contact-right { left: 414px; }
  .letter-date {
    position: absolute; left: 62px; top: 282px;
    font-family: "Open Sans", sans-serif; font-weight: 500; color: var(--ink); font-size: 14.5px;
  }
</style>
</head>
<body>
<div class="letterhead">
  <div class="top-band" role="img" aria-label="Green light streak decoration along the top edge"></div>
  <div class="side-band" role="img" aria-label="Vertical green light streak decoration along the left edge"></div>
  <main class="page">
    <header class="brand">
      <div class="brand-square"></div>
      <div class="brand-text">
        <div class="brand-name">HARLOW CHAMBERS</div>
        <div class="brand-tagline">Barristers and Mediators</div>
      </div>
    </header>
    <ul class="contact contact-left">
      <li>Barrister- At-Law LL.B.</li>
      <li>ABN 51 607 219 004</li>
      <li>HARLOW CHAMBERS</li>
      <li>LEVEL 1 28 HARLOW STREET, EASTON</li>
      <li>P.O. BOX 712, EASTON. Q. 4870</li>
    </ul>
    <ul class="contact contact-right">
      <li>Barrister- At-Law LL.B.</li>
      <li>ABN 51 607 219 004</li>
      <li>HARLOW CHAMBERS</li>
      <li>LEVEL 1 28 HARLOW STREET, EASTON</li>
      <li>P.O. BOX 712, EASTON. Q. 4870</li>
    </ul>
    <p class="letter-date">6 November 2015</p>
  </main>
</div>
</body>
</html>
```